Email signature

I am looking for an innovative and classy looking email signature that I can use with gmail.

My info:

Dale Bowen
618.442.9037
j.dale.bowen@fernmail.com
www.NorthRidgeArcheryClub.com

My logo and business card files are attached.

Font:
- Serpentine-Bold-Bold for "NORTH RIDGE"
- BrowalliaUPC for "ARCHERY CLUB"

Colors (CMYK code):
- BLACK ....... 0; 0; 0; 100;
- ORANGE ... gradient from 0; 65; 97.5; 0 to 0; 39; 97.5; 0

Dale Bowen

North Ridge Archery Club

j.dale.bowen@fernmail.com

618.442.9037

```html
<!DOCTYPE html>
<html lang="en">
<head>
<meta charset="utf-8">
<title>Dale Bowen — Email Signature</title>
<link href="https://fonts.googleapis.com/css2?family=Bebas+Neue&family=Oswald:wght@500&family=Noto+Sans+Mono:wght@400&display=swap" rel="stylesheet">
<style>
  :root {
    --ink: #3a3a3a;
    --text: #555555;
    --orange: #f28c28;
    --orange-deep: #ee7a1e;
    --rule: #444444;
    --paper: #ffffff;
  }
  html, body {
    margin: 0;
    padding: 0;
    width: 1200px;
    height: 1000px;
    overflow: hidden;
    background: var(--paper);
  }
  .signature {
    position: relative;
    width: 1200px;
    height: 1000px;
  }
  .brand-mark {
    position: absolute;
    left: 205px;
    top: 384px;
    width: 175px;
    text-align: center;
  }
  .brand-mark__dot {
    display: block;
    width: 96px;
    height: 96px;
    margin: 0 auto 10px;
    border-radius: 50%;
    background: linear-gradient(180deg, var(--orange-deep), var(--orange));
  }
  .brand-mark__name {
    font-family: "Noto Sans Mono", monospace;
    font-size: 15px;
    line-height: 19px;
    color: var(--ink);
  }
  .holder-name {
    position: absolute;
    left: 380px;
    top: 388px;
    margin: 0;
    font-family: "Bebas Neue", sans-serif;
    font-weight: 400;
    font-size: 84px;
    line-height: 84px;
    letter-spacing: 1px;
    color: var(--ink);
  }
  .label {
    position: absolute;
    font-family: "Oswald", sans-serif;
    font-weight: 500;
    font-size: 13px;
    line-height: 16px;
    text-transform: uppercase;
    color: var(--orange);
    letter-spacing: 0.2px;
  }
  .value {
    position: absolute;
    font-family: "Noto Sans Mono", monospace;
    color: var(--text);
    white-space: nowrap;
  }
  .value--lg { font-size: 17.5px; line-height: 22px; }
  .value--sm { font-size: 15px; line-height: 20px; }
  .divider {
    position: absolute;
    left: 735px;
    top: 463px;
    width: 1px;
    height: 53px;
    background: var(--rule);
  }
  .baseline {
    position: absolute;
    top: 535px;
    height: 1px;
    background: var(--rule);
  }
</style>
</head>
<body>
<div class="signature">
  <div class="brand-mark">
    <span class="brand-mark__dot"></span>
    <div class="brand-mark__name">North Ridge<br>Archery Club</div>
  </div>

  <h1 class="holder-name">Dale Bowen</h1>

  <span class="label" style="left:383px; top:470px;">Company</span>
  <span class="value value--lg" style="left:444px; top:465px;">North Ridge Archery Club</span>

  <span class="label" style="left:384px; top:497px;">Site</span>
  <span class="value value--sm" style="left:445px; top:495px;">www.NorthRidgeArcheryClub.com</span>

  <div class="divider"></div>

  <span class="label" style="left:753px; top:468px;">Email</span>
  <span class="value value--lg" style="left:800px; top:463px;">j.dale.bowen@fernmail.com</span>

  <span class="label" style="left:753px; top:496px;">Phone</span>
  <span class="value value--lg" style="left:802px; top:491px;">618.442.9037</span>

  <div class="baseline" style="left:211px; width:47px;"></div>
  <div class="baseline" style="left:328px; width:743px;"></div>
</div>
</body>
</html>
```